Brackwell Engineering Inc. Marketing Brochure

need a brochure designed for Brackwell Engineering Inc. It would follow the theme of www.brackwelleng.ca. It would be ~7" x 9" in size. Full Color. 4 pages. Please refer to BrackwellENG.ca to get the description of our services. The text font will be in the attached documents also. The theme must be industrial but also smart telling the customer that we use the latest in 3d cadworx to build our facilities. https://www.lookvarne.ca/find?q=3d+cadworx+images&type=img&src=qx&ctx=1&ref=MqTrodLP48vnzaX%253A%252C_2p9HbeW_4kjsT%252C_&tok=ZkwpRmq83LuxnVD-KolQW71-h3pjk_PRat&sa=Y&vid=9bhPRmxTy4kLmWf8KbQn1jLqPwRtsYcVb4HkTzXqW2pDcGhWqY#imgid=RK8M_4x2pzqm7N:&imgref=MqTrodLP48vnzaX:

Industry/Entity Type

Oil And Gas Exploration

Requirements
Must have
• a 7" x 9" brochure that is snappy, smart and crisp along the same lines at the brackwelleng.ca website.
Nice to have
• it must include the "services" listed on the brackwelleng.ca website
• It must really highlight the brand of name Brackwell Engineering Inc. AND the polar bear.
• Mission Statement: Brackwell Engineering Inc. offers fit-for-purpose, pragmatic EPCM (Engineering, Procurement and Construction Management) and Asset Management Consulting (MOC) in a timely, cost effective manner built on the foundations of safety, environmental protection and cost control.
Should not have
• it must not be too overly "wordy". We are selling an IMAGE and a BRAND here more than anything.
• Remove/do not include the Brackwell Engineering is Back paragraph... I want to move my messaging away from that theme.

```html
<!DOCTYPE html>
<html lang="en">
<head>
<meta charset="utf-8">
<title>Brackwell Engineering Inc. – Services Spread</title>
<link href="https://fonts.googleapis.com/css2?family=Montserrat:wght@400;500;600;700;800&display=swap" rel="stylesheet">
<style>
  :root {
    --backdrop: #4d5260;
    --strip: #8ea8d0;
    --heading-pale: #c3d2ea;
    --ink-light: #dfe6f0;
    --ink-white: #ffffff;
    --ink-dark: #2a2d33;
    --rule: #8d9ab0;
  }
  * { margin: 0; padding: 0; box-sizing: border-box; }
  html, body {
    width: 1200px; height: 864px; overflow: hidden;
    background: var(--backdrop);
    font-family: "Montserrat", sans-serif;
  }
  .spread {
    position: absolute; left: 40px; top: 72px;
    width: 1120px; height: 720px;
    box-shadow: 0 20px 50px rgba(0,0,0,.35);
  }
  .spread-art { position: absolute; inset: 0; }
  .services-title {
    position: absolute; left: 84px; top: 110px;
    font-weight: 700; font-size: 31px; line-height: 40px;
    letter-spacing: 1px; color: var(--heading-pale);
  }
  .service-group { position: absolute; color: var(--ink-light); }
  .service-group h3 {
    font-weight: 700; font-size: 19px; line-height: 24px;
    color: var(--ink-white); margin-bottom: 10px; letter-spacing: .3px;
    white-space: nowrap;
  }
  .service-group li {
    list-style: none; font-size: 15px; font-weight: 400;
    line-height: 19px; margin-bottom: 17px; white-space: nowrap;
  }
  .service-group li:last-child { margin-bottom: 0; }
  .group-epcm { left: 322px; top: 60px; width: 200px; }
  .group-asset { left: 588px; top: 70px; width: 240px; }
  .group-automation { left: 866px; top: 56px; width: 230px; }
  .group-automation li { margin-bottom: 12px; }
  .group-asbuilding { left: 874px; top: 232px; width: 230px; }
  .group-asbuilding li { margin-bottom: 12px; }
  .contact-title {
    position: absolute; left: 420px; top: 526px;
    font-weight: 800; font-size: 36px; color: var(--ink-dark);
  }
  .contact-item {
    position: absolute; display: flex; align-items: flex-start; gap: 12px;
    color: var(--ink-white); font-size: 17px; line-height: 21px; font-weight: 500;
    white-space: nowrap;
  }
  .contact-item svg { flex: none; margin-top: 1px; }
  .contact-phone { left: 336px; top: 594px; }
  .contact-address { left: 336px; top: 628px; }
  .contact-email { left: 610px; top: 592px; }
  .contact-web { left: 610px; top: 632px; }
</style>
</head>
<body>
<main class="spread">
  <svg class="spread-art" width="1120" height="720" viewBox="0 0 1120 720">
    <defs>
      <radialGradient id="pageGlow" cx="0.55" cy="0.6" r="0.6">
        <stop offset="0" stop-color="#e4e9f1"/>
        <stop offset="0.5" stop-color="#b9c7de"/>
        <stop offset="1" stop-color="#8ea5cb"/>
      </radialGradient>
      <linearGradient id="panelShade" x1="0" y1="0" x2="1" y2="0.4">
        <stop offset="0" stop-color="#262c36"/>
        <stop offset="0.5" stop-color="#3a4555"/>
        <stop offset="1" stop-color="#56677e"/>
      </linearGradient>
      <linearGradient id="arrowFill" x1="0" y1="0" x2="1" y2="0">
        <stop offset="0" stop-color="#4f7dbd"/>
        <stop offset="1" stop-color="#a9bfe0"/>
      </linearGradient>
      <linearGradient id="plantTone" x1="0" y1="0" x2="0" y2="1">
        <stop offset="0" stop-color="#2c4258"/>
        <stop offset="0.45" stop-color="#5f7a8e"/>
        <stop offset="0.75" stop-color="#c9d3dc"/>
        <stop offset="1" stop-color="#9aa8b4"/>
      </linearGradient>
      <linearGradient id="barFill" x1="0" y1="0" x2="1" y2="0">
        <stop offset="0" stop-color="#2579bd"/>
        <stop offset="1" stop-color="#12609f"/>
      </linearGradient>
    </defs>

    <rect class="page-base" width="1120" height="720" fill="url(#pageGlow)"/>

    <g class="plant-photo" role="img" aria-label="Night view of a gas processing plant with lit storage domes and piping">
      <polygon points="560,470 620,410 1120,410 1120,470 900,720 360,720" fill="url(#plantTone)"/>
    </g>
    <polygon class="corner-tint" points="1120,470 1120,720 900,720" fill="#8ea5cb"/>

    <polygon class="services-panel" points="0,24 1120,24 1120,410 0,410" fill="url(#panelShade)"/>
    <rect class="top-strip" x="0" y="0" width="1120" height="24" fill="var(--strip)"/>

    <polygon class="arrow-block" points="0,0 110,0 302,172 0,432" fill="url(#arrowFill)"/>
    <polyline class="arrow-outline" points="112,0 306,172 0,436" fill="none" stroke="#e7edf6" stroke-width="6"/>

    <line class="column-rule" x1="540" y1="90" x2="540" y2="392" stroke="var(--rule)" stroke-width="1.5"/>
    <line class="column-rule" x1="848" y1="56" x2="848" y2="392" stroke="var(--rule)" stroke-width="1.5"/>

    <line class="fold" x1="560" y1="0" x2="560" y2="720" stroke="rgba(255,255,255,.18)" stroke-width="1"/>

    <polygon class="contact-bar" points="326,572 902,572 818,682 220,682" fill="url(#barFill)"/>
  </svg>

  <h2 class="services-title">OUR<br>SERVICES</h2>

  <section class="service-group group-epcm">
    <h3>EPCM</h3>
    <ul>
      <li>Oil &amp; Gas Pipelines</li>
      <li>Debottlenecking</li>
      <li>Compression</li>
      <li>Refrigeration</li>
      <li>Oil Batteries</li>
      <li>Hazops</li>
      <li>Process Reviews<br>and capacity studies</li>
    </ul>
  </section>

  <section class="service-group group-asset">
    <h3>Asset Management</h3>
    <ul>
      <li>Management of Change (MOC)</li>
      <li>EPAP Programs</li>
      <li>Maintainance<br>Management</li>
      <li>Integrity Management</li>
      <li>Regulatory Submissions</li>
      <li>Suspended Well<br>Programs</li>
    </ul>
  </section>

  <section class="service-group group-automation">
    <h3>Automation</h3>
    <ul>
      <li>PLC's</li>
      <li>RTU's</li>
      <li>Control Systems</li>
      <li>Field Programming</li>
    </ul>
  </section>

  <section class="service-group group-asbuilding">
    <h3>As-Building</h3>
    <ul>
      <li>3D Site &amp; Piping</li>
      <li>Laser Scanning</li>
      <li>Complete As-Built<br>Site Drawing Package</li>
    </ul>
  </section>

  <h2 class="contact-title">Contact Us</h2>

  <div class="contact-item contact-phone">
    <svg width="20" height="20" viewBox="0 0 24 24" fill="#fff"><path d="M6.6 10.8a15.1 15.1 0 0 0 6.6 6.6l2.2-2.2a1 1 0 0 1 1-.25 11.4 11.4 0 0 0 3.6.57 1 1 0 0 1 1 1V20a1 1 0 0 1-1 1A17 17 0 0 1 3 4a1 1 0 0 1 1-1h3.5a1 1 0 0 1 1 1c0 1.25.2 2.45.57 3.57a1 1 0 0 1-.25 1z"/></svg>
    <span>(555) 014-2270</span>
  </div>
  <div class="contact-item contact-address">
    <svg width="20" height="22" viewBox="0 0 24 26" fill="none" stroke="#fff" stroke-width="2.4"><path d="M12 24s-8-8-8-14a8 8 0 0 1 16 0c0 6-8 14-8 14z"/><circle cx="12" cy="10" r="3"/></svg>
    <span>Brackwell Engineering Inc.<br>Calgary, Alberta, Canada</span>
  </div>
  <div class="contact-item contact-email">
    <svg width="22" height="18" viewBox="0 0 24 18" fill="none" stroke="#fff" stroke-width="2"><rect x="1" y="1" width="22" height="16" rx="1"/><path d="M1 1l11 9 11-9"/></svg>
    <span>contactus@brackwelleng.ca</span>
  </div>
  <div class="contact-item contact-web">
    <svg width="22" height="22" viewBox="0 0 24 24" fill="none" stroke="#fff" stroke-width="2"><circle cx="12" cy="12" r="10"/><path d="M2 12h20M12 2a15 15 0 0 1 0 20M12 2a15 15 0 0 0 0 20"/></svg>
    <span>BrackwellEng.ca</span>
  </div>
</main>
</body>
</html>
```